RJ Penhall & Associates

Create a website encompassing design work already carried out for business card.
Small accounting practice, business accounting and management, superannuation, audit, taxation.

```html
<!DOCTYPE html>
<html lang="en">
<head>
<meta charset="utf-8">
<title>RJ Penhall &amp; Associates</title>
<link href="https://fonts.googleapis.com/css2?family=Libre+Baskerville:wght@400;700&family=Hind:wght@400;600;700&family=Open+Sans:wght@600;700&display=swap" rel="stylesheet">
<style>
:root{
  --page-bg:#f1f1f1;
  --panel:#ffffff;
  --header:#181818;
  --sky:#45aee3;
  --accent:#12a5e6;
  --link:#1aa3dc;
  --ink:#333333;
  --body:#444444;
  --muted:#777777;
  --nav-top:#a6a6a6;
  --nav-bottom:#6e6e6e;
  --rule:#dddddd;
  --dark-tag:#444444;
}
*{box-sizing:border-box;margin:0;padding:0}
html,body{width:1141px;height:1200px;overflow:hidden}
body{background:var(--page-bg);font-family:"Hind",sans-serif;color:var(--body);position:relative}
.site{position:absolute;left:91px;top:0;width:959px;height:1113px;background:var(--panel);box-shadow:0 0 3px rgba(0,0,0,.15)}
.masthead{position:absolute;left:0;top:0;width:959px;height:101px;background:var(--header)}
.brand{position:absolute;left:73px;top:22px;display:flex;align-items:center;gap:14px}
.brand-square{width:54px;height:54px;background:var(--sky)}
.brand-name{font-family:"Libre Baskerville",serif;color:#fff;font-size:22px;line-height:23px;font-weight:400}
.phone{position:absolute;right:20px;top:30px;color:var(--sky);font-size:15px;display:flex;align-items:center;gap:6px}
.social{position:absolute;right:26px;top:63px;display:flex;gap:6px}
.social span{width:21px;height:21px;border-radius:50%;display:block}
.tagline{position:absolute;left:0;top:101px;width:959px;height:26px;background:var(--sky);color:#fff;font-family:"Open Sans",sans-serif;font-weight:600;font-size:9px;line-height:26px;padding-left:24px}
.main-nav{position:absolute;left:0;top:127px;width:959px;height:41px;background:linear-gradient(var(--nav-top),var(--nav-bottom));display:flex;box-shadow:0 4px 6px rgba(0,0,0,.12)}
.main-nav a{color:#fff;text-decoration:none;font-family:"Open Sans",sans-serif;font-weight:700;font-size:13px;line-height:41px;padding:0 25px;border-right:1px solid rgba(0,0,0,.25);box-shadow:1px 0 0 rgba(255,255,255,.25)}
.main-nav a:first-child{padding-left:22px}
.main-nav a:last-child{border:none;box-shadow:none}
.hero{position:absolute;left:21px;top:188px;width:917px;height:301px;border-radius:5px;background:radial-gradient(ellipse at 70% 55%,#5d8fd0 0%,#8cb4dd 18%,#c9dde9 45%,#e2ecf0 70%,#bfe0ef 100%)}
.hero-line{position:absolute;left:26px;font-family:"Libre Baskerville",serif;color:#fff;font-size:19px;padding:0 10px;height:41px;line-height:41px}
.hero-line.one{top:123px;background:var(--sky)}
.hero-line.two{top:166px;background:var(--dark-tag)}
.welcome{position:absolute;left:22px;top:508px;width:915px}
.welcome h1{font-family:"Libre Baskerville",serif;font-weight:700;font-size:26px;color:var(--ink);margin-bottom:8px}
.welcome p{font-size:14px;line-height:24px}
.welcome a{color:var(--link);text-decoration:none;font-size:14px;line-height:24px}
.card{position:absolute;top:660px;width:294px;height:304px;border:1px solid var(--rule);border-radius:4px;background:linear-gradient(#fff 55%,#ececec)}
.card h2{font-family:"Libre Baskerville",serif;font-weight:700;font-size:25px;color:var(--ink);position:absolute;top:18px}
.services{left:25px}.news{left:336px}.reviews{left:646px}
.service-list{position:absolute;left:22px;top:62px;width:256px;list-style:none}
.service-list li{height:38.5px;display:flex;align-items:center;gap:10px;font-size:14px;color:var(--ink);border-bottom:1px solid var(--rule)}
.service-list li:last-child{border:none}
.service-list i{width:22px;height:22px;border-radius:50%;background:#f0f0f0;border:1px solid #d8d8d8;display:block}
.news-body{position:absolute;left:29px;top:64px;width:240px;font-size:13.5px;line-height:22px;color:var(--ink)}
.news-body time{display:block;font-size:12.5px;color:var(--muted)}
.news-body b{display:block;margin-top:2px}
.news-body p+time{margin-bottom:4px}
.review-body{position:absolute;left:26px;top:66px;width:250px;font-size:14px;line-height:24px;color:var(--ink)}
.review-body cite{display:block;margin-top:6px;font-weight:700;font-style:italic}
.btn{position:absolute;top:272px;height:30px;line-height:31px;padding:0 14px;background:var(--accent);color:#fff;font-weight:700;font-size:14px;border-radius:3px;text-decoration:none}
.partners{position:absolute;left:40px;top:1002px;width:880px;display:flex;justify-content:space-between;align-items:center}
.partners span{display:block;background:#dedede}
.site-footer{position:absolute;left:0;top:1126px;width:1141px;text-align:center;color:var(--body);font-size:14px}
.site-footer nav a{color:var(--body);text-decoration:none;margin:0 9px}
.site-footer p{margin-top:6px}
</style>
</head>
<body>
<div class="site">
  <header class="masthead">
    <div class="brand"><span class="brand-square"></span><span class="brand-name">RJ Penhall<br>&amp; Associates.</span></div>
    <div class="phone">
      <svg width="10" height="16" viewBox="0 0 10 16"><path d="M7 1 C2 3 1 12 6 15 L8 12 C5 10 5 6 8 4 Z" fill="#45aee3"/></svg>
      +1 (555) 014 2270
    </div>
    <div class="social"><span style="background:#3b5998"></span><span style="background:#2aa9e0"></span><span style="background:#0e76a8"></span><span style="background:#c4302b"></span></div>
  </header>
  <div class="tagline">Accountant &nbsp;·&nbsp; Business Solutions &nbsp;·&nbsp; Management &nbsp;·&nbsp; Superannuation &nbsp;·&nbsp; Audit</div>
  <nav class="main-nav"><a>HOME</a><a>ABOUT US</a><a>SERVICES</a><a>LATEST NEWS</a><a>TESTIMONIALS</a><a>FAQ</a><a>CONTACT US</a></nav>

  <section class="hero" role="img" aria-label="Photo of a businessman holding a glowing globe surrounded by business icons">
    <div class="hero-line one">Build Your Own Future</div>
    <div class="hero-line two">With Our Expertise</div>
  </section>

  <section class="welcome">
    <h1>Welcome to</h1>
    <p>Lorem Ipsum is simply dummy text of the printing and typesetting industry. Lorem Ipsum has been the industry's standard dummy text ever since the 1500s, when an unknown printer took a galley of type and scrambled it to make a type specimen book. It has survived not only five centuries, but also the leap into electronic typesetting, remaining essentially unchanged. It was popularised in the 1960s with the release of Letraset .</p>
    <a href="#">Click Here</a>
  </section>

  <article class="card services">
    <h2 style="left:20px">Our Services</h2>
    <ul class="service-list">
      <li><i></i>Accounting</li>
      <li><i></i>Business Management</li>
      <li><i></i>Audit</li>
      <li><i></i>Superannuation</li>
      <li><i></i>Tax</li>
    </ul>
    <a class="btn" href="#" style="left:24px">Know More</a>
  </article>

  <article class="card news">
    <h2 style="left:27px">Latest News</h2>
    <div class="news-body">
      <time>13/09/2014</time>
      <b>Lorem Ipsum is simply dummy</b>
      <p>text of the printing and typesetting industry. Lorem Ipsum .</p>
      <time>13/09/2014</time>
      <b>Lorem Ipsum is simply dummy</b>
      <p>text of the printing and typesetting industry. Lorem Ipsum .</p>
    </div>
    <a class="btn" href="#" style="left:29px">Know More</a>
  </article>

  <article class="card reviews">
    <h2 style="left:21px">Testimonials</h2>
    <div class="review-body">
      Lorem Ipsum is simply dummy text of the printing and typesetting industry. Lorem Ipsum has been the industry's standard dummy text ever since the 1500s, when an unknown printer took a galley of type and scrambled.
      <cite>Sam, Leeds</cite>
    </div>
    <a class="btn" href="#" style="left:29px">Know More</a>
  </article>

  <div class="partners">
    <span style="width:90px;height:40px"></span>
    <span style="width:104px;height:40px"></span>
    <span style="width:86px;height:40px"></span>
    <span style="width:102px;height:40px"></span>
    <span style="width:116px;height:22px"></span>
    <span style="width:126px;height:20px"></span>
  </div>
</div>

<footer class="site-footer">
  <nav><a>Home</a><a>About us</a><a>Services</a><a>Latest News</a><a>Testimonials</a><a>Contact Us</a></nav>
  <p>Copyright © 2014 RJ Penhall &amp; Associates. All rights reserved.</p>
</footer>
</body>
</html>
```